Business Postcard Mailer - 2 sided - 6 x 10.5 inches

We will be purchasing multiple designs through this project. We need a postcard mailer for a residential painting business. The final design needs to have the special 15% Off, contact information, company logo, stamp indicia, and list of services. I will provide past examples and any additional logos. Company colors are #34482E and #4A1717. Old samples are provided. Final flat size should be 6 x 10.5 inches. And we will need a return address in the upper left-hand corner of the backside. QMRB Layout Guidelines are attached. 4389 Juniper Ave #7, Waukesha, WI 53947.
Updates

I just guaranteed the project and will be expecting more entries. We will also be purchasing additional designs (4-5) so we want to ensure a good variety.

Target Market(s)

Homeowners

Industry/Entity Type

Painting

Font styles to use
Sans Serif

Requirements
Must have
• Logo and brand colors
Nice to have
• Call to action - Book your free estimate at www.BrightCoatCrew.example or Call now 262-555-0147.

```html
<!DOCTYPE html>
<html lang="en">
<head>
<meta charset="utf-8">
<title>BrightCoat Crew Postcard Mailer</title>
<link href="https://fonts.googleapis.com/css2?family=Oswald:wght@500&family=Roboto:wght@400;500;700&display=swap" rel="stylesheet">
<style>
  :root {
    --green: #34482E;
    --maroon: #4A1717;
    --paper: #ffffff;
    --stage: #dedede;
    --ink: #1e1e1e;
    --badge: #9a9a9a;
    --rule: #555555;
  }
  * { margin: 0; padding: 0; box-sizing: border-box; }
  html, body { width: 1200px; height: 1200px; overflow: hidden; }
  body { background: var(--stage); position: relative; font-family: "Roboto", sans-serif; color: var(--ink); }
  .card { position: absolute; left: 216px; width: 769px; height: 445px; background: var(--paper); overflow: hidden; }
  .front { top: 113px; }
  .back { top: 641px; }
  .abs { position: absolute; }

  /* front */
  .top-band { left: 0; top: 0; width: 769px; height: 25px; background: var(--maroon); }
  .title-band { left: 0; top: 25px; width: 769px; height: 56px; background: var(--green); }
  .title { left: 230px; width: 539px; top: 25px; height: 56px; line-height: 56px; text-align: center;
    font-family: "Oswald", sans-serif; font-weight: 500; font-size: 46px; color: #fff; letter-spacing: 0.5px; }
  .logo-box { left: 24px; top: 0; width: 160px; height: 108px; background: var(--paper);
    display: flex; align-items: center; justify-content: center; gap: 8px; }
  .logo-name { font-family: "Roboto", sans-serif; font-weight: 700; color: var(--green); font-size: 22px; line-height: 1.05; }
  .logo-mark { width: 14px; height: 14px; background: var(--maroon); flex: none; }
  .scene-back { left: 280px; top: 81px; width: 281px; height: 300px;
    background: linear-gradient(180deg, #5a6470 0%, #3c4a3a 55%, #4d6a34 100%); }
  .hero-photo { left: 0; top: 81px; width: 442px; height: 230px;
    background: linear-gradient(180deg, #b9c6d4 0%, #9ea392 45%, #7c7a66 100%); border-right: 2px solid var(--maroon); }
  .hero-caption { left: 0; top: 281px; width: 442px; height: 30px; background: rgba(40,40,40,0.7);
    color: #fff; font-weight: 500; font-size: 19px; line-height: 30px; text-align: center; }
  .services { left: 561px; top: 81px; width: 208px; height: 172px; background: var(--paper); padding: 15px 0 0 18px; }
  .services li { list-style: none; font-weight: 500; font-size: 17px; line-height: 24.3px; color: var(--green);
    display: flex; align-items: center; gap: 5px; white-space: nowrap; }
  .services svg { width: 15px; height: 15px; flex: none; }
  .kitchen-photo { left: 561px; top: 253px; width: 208px; height: 128px;
    background: linear-gradient(180deg, #d9d6d0 0%, #eeeeec 50%, #8c8579 100%); }
  .special-box { left: 0; top: 311px; width: 280px; height: 134px; background: var(--paper); color: var(--maroon);
    padding: 8px 0 0 52px; font-weight: 700; font-size: 50px; line-height: 58px; }
  .phone-band { left: 280px; top: 387px; width: 489px; height: 58px; background: var(--maroon);
    display: flex; align-items: center; justify-content: center; gap: 8px;
    color: #fff; font-weight: 700; font-size: 34px; }
  .phone-band svg { width: 26px; height: 26px; }

  /* back */
  .return-panel { left: 0; top: 0; width: 347px; height: 445px; }
  .address { left: 25px; top: 22px; display: flex; gap: 10px; font-size: 19px; line-height: 24px; color: var(--ink); }
  .address svg { width: 18px; height: 18px; margin-top: 2px; flex: none; }
  .blurb { left: 25px; top: 72px; width: 316px; font-size: 11.5px; font-weight: 500; line-height: 15px; text-align: justify; }
  .home-photo { left: 0; top: 113px; width: 347px; height: 111px;
    background: linear-gradient(180deg, #a8b4c2 0%, #a78b70 50%, #5e5040 100%); }
  .special-small { left: 26px; top: 232px; color: var(--maroon); font-weight: 700; font-size: 34px; line-height: 40px; }
  .badges { left: 175px; top: 236px; width: 165px; display: grid; grid-template-columns: 72px 36px 40px; gap: 10px 8px; }
  .badge { height: 24px; background: var(--badge); border-radius: 3px; }
  .badge.round { border-radius: 50%; width: 24px; justify-self: center; }
  .contact-band { left: 0; top: 309px; width: 347px; height: 136px; background: var(--maroon); color: #fff; padding: 10px 0 0 26px; }
  .contact-phone { display: flex; align-items: center; gap: 10px; font-weight: 700; font-size: 36px; line-height: 46px; }
  .contact-phone svg { width: 30px; height: 30px; }
  .contact-line { display: flex; align-items: center; gap: 14px; font-size: 19px; line-height: 32px; margin-left: 6px; white-space: nowrap; }
  .contact-line svg { width: 18px; height: 18px; flex: none; }
  .divider { left: 347px; top: 0; width: 13px; height: 445px; background: var(--green); }
  .mail-logo { left: 464px; top: 36px; display: flex; align-items: center; gap: 6px; }
  .mail-logo .logo-name { font-size: 18px; }
  .mail-logo .logo-mark { width: 11px; height: 11px; }
  .indicia { left: 672px; top: 25px; width: 69px; height: 70px; border: 2px solid var(--ink);
    text-align: center; font-size: 8.5px; line-height: 10.5px; padding-top: 4px; }
  .indicia .paid { font-weight: 700; font-size: 11px; border-top: 1px solid var(--ink); border-bottom: 1px solid var(--ink); margin: 2px 4px; line-height: 13px; }
  .address-line { left: 510px; width: 232px; height: 1px; background: var(--rule); }
</style>
</head>
<body>

<section class="card front">
  <div class="abs top-band"></div>
  <div class="abs title-band"></div>
  <h1 class="abs title">BRIGHTCOAT CREW</h1>
  <div class="abs scene-back" role="img" aria-label="Photo of a residential street with houses and trees at dusk"></div>
  <div class="abs hero-photo" role="img" aria-label="Photo of a freshly painted two-storey house with a white-columned porch"></div>
  <div class="abs hero-caption">Locally Owned and Operated</div>
  <div class="abs logo-box">
    <span class="logo-name">BrightCoat<br>Crew</span>
    <span class="logo-mark"></span>
  </div>
  <ul class="abs services">
    <li><svg viewBox="0 0 16 16"><path d="M2 8.5l4 4 8-9" fill="none" stroke="#1e1e1e" stroke-width="2.4"/></svg>Interior Painting</li>
    <li><svg viewBox="0 0 16 16"><path d="M2 8.5l4 4 8-9" fill="none" stroke="#1e1e1e" stroke-width="2.4"/></svg>Exterior Painting</li>
    <li><svg viewBox="0 0 16 16"><path d="M2 8.5l4 4 8-9" fill="none" stroke="#1e1e1e" stroke-width="2.4"/></svg>Carpentry Services</li>
    <li><svg viewBox="0 0 16 16"><path d="M2 8.5l4 4 8-9" fill="none" stroke="#1e1e1e" stroke-width="2.4"/></svg>Drywall Repair</li>
    <li><svg viewBox="0 0 16 16"><path d="M2 8.5l4 4 8-9" fill="none" stroke="#1e1e1e" stroke-width="2.4"/></svg>Color Consultations</li>
    <li><svg viewBox="0 0 16 16"><path d="M2 8.5l4 4 8-9" fill="none" stroke="#1e1e1e" stroke-width="2.4"/></svg>Financing Available</li>
  </ul>
  <div class="abs kitchen-photo" role="img" aria-label="Photo of a bright white kitchen with an island and pendant lights"></div>
  <div class="abs special-box">Special<br>15% Off</div>
  <div class="abs phone-band">
    <svg viewBox="0 0 24 24"><circle cx="12" cy="12" r="12" fill="#fff"/><path d="M8.2 5.5l2 2.8-1.3 1.6c.9 1.9 2.4 3.4 4.2 4.3l1.6-1.3 2.8 2-1 2.4c-5.3-.6-9.3-4.6-9.9-9.8z" fill="#4A1717"/></svg>
    262-555-0147
  </div>
</section>

<section class="card back">
  <div class="abs return-panel"></div>
  <div class="abs address">
    <svg viewBox="0 0 18 18"><circle cx="9" cy="9" r="9" fill="#1e1e1e"/><circle cx="9" cy="7.5" r="2.6" fill="none" stroke="#fff" stroke-width="1.4"/><path d="M9 10.3v3.6M6 13.9h6" stroke="#fff" stroke-width="1.4"/></svg>
    <span>4389 Juniper Ave #7, Waukesha,<br>WI 53947</span>
  </div>
  <p class="abs blurb">We cater the size of the crew to the size of the job and workfull continuous days until the project is complete.</p>
  <div class="abs home-photo" role="img" aria-label="Photo of a brick and stone family home with a front lawn"></div>
  <div class="abs special-small">Special<br>15% Off</div>
  <div class="abs badges" aria-hidden="true">
    <div class="badge"></div><div class="badge"></div><div class="badge"></div>
    <div class="badge"></div><div class="badge"></div><div class="badge round"></div>
  </div>
  <div class="abs contact-band">
    <div class="contact-phone">
      <svg viewBox="0 0 24 24"><circle cx="12" cy="12" r="12" fill="#fff"/><path d="M8.2 5.5l2 2.8-1.3 1.6c.9 1.9 2.4 3.4 4.2 4.3l1.6-1.3 2.8 2-1 2.4c-5.3-.6-9.3-4.6-9.9-9.8z" fill="#4A1717"/></svg>
      262-555-0147
    </div>
    <div class="contact-line">
      <svg viewBox="0 0 18 18" fill="none" stroke="#fff" stroke-width="1.3"><circle cx="9" cy="9" r="8"/><ellipse cx="9" cy="9" rx="3.5" ry="8"/><path d="M1 9h16M2.5 5h13M2.5 13h13"/></svg>
      www.BrightCoatCrew.example
    </div>
    <div class="contact-line">
      <svg viewBox="0 0 18 18"><circle cx="9" cy="9" r="9" fill="#fff"/><rect x="4.5" y="6" width="9" height="6.5" fill="none" stroke="#4A1717" stroke-width="1.3"/><path d="M4.5 6l4.5 3.5L13.5 6" fill="none" stroke="#4A1717" stroke-width="1.3"/></svg>
      crew@brightcoat.example
    </div>
  </div>
  <div class="abs divider"></div>
  <div class="abs mail-logo">
    <span class="logo-name">BrightCoat<br>Crew</span>
    <span class="logo-mark"></span>
  </div>
  <div class="abs indicia">
    Presorted<br>Standard<br>U.S. Postage
    <div class="paid">PAID</div>
    NPX
  </div>
  <div class="abs address-line" style="top:187px"></div>
  <div class="abs address-line" style="top:216px"></div>
  <div class="abs address-line" style="top:244px"></div>
  <div class="abs address-line" style="top:273px"></div>
  <div class="abs address-line" style="top:301px"></div>
  <div class="abs address-line" style="top:329px"></div>
</section>

</body>
</html>
```